Poster Design Project

We are a pizzeria based in Sydney CBD. Please see attached file for new website, do not use the current website look to make your graphic design.

We want to run a promotional campaign called " Rustico Rush".

Rustico Rush
$9 Pizza

Crispy & fresh dough topped with mouth watering mozzarella cheese, sprinkled with oregano and finished with fresh basil.

takeaway & eat in only
Medium Pizza Only (11 inch)

Target Market(s)

It is the lunch crowd in sydney cbd, predominately male but some female too. targeting the office workers.

Industry/Entity Type

Graphic Design

Requirements
Must have
• We are an Italian Pizzeria, so we would like an italian look and feel
our unique advantage is authentic and delicious thin crispy pizza
we want a nostalgic look and feel
some examples are attached of colours and style we like
Nice to have
• I can send you via email files to show you what the new website will look like

```html
<!DOCTYPE html>
<html lang="en">
<head>
<meta charset="utf-8">
<title>Rustico Rush – $9 Pizza</title>
<link rel="stylesheet" href="https://fonts.googleapis.com/css2?family=Alfa+Slab+One&family=Kaushan+Script&family=Fredoka:wght@600;700&family=Parisienne&family=Archivo+Black&display=swap">
<style>
  :root {
    --bg-deep: #1e0e06;
    --bg-mid: #4a230f;
    --bg-warm: #9a5326;
    --band: #2e1509;
    --title-orange: #f4a023;
    --title-gold: #f9bd45;
    --price-yellow: #f7b520;
    --ink: #111111;
    --white: #ffffff;
    --cream: #fff4e2;
  }
  * { margin: 0; padding: 0; box-sizing: border-box; }
  html, body { width: 848px; height: 1200px; overflow: hidden; background: var(--bg-deep); }
  .poster {
    position: relative;
    width: 848px;
    height: 1200px;
    overflow: hidden;
    background:
      radial-gradient(ellipse 60% 40% at 45% 62%, rgba(200,110,50,0.55) 0%, rgba(200,110,50,0) 100%),
      linear-gradient(180deg, var(--bg-deep) 0%, var(--bg-mid) 40%, var(--bg-warm) 60%, var(--bg-mid) 85%, var(--bg-deep) 100%);
  }
  .photo { position: absolute; }
  .photo--hero {
    left: 0; top: 0; width: 848px; height: 470px;
    background:
      radial-gradient(ellipse 22% 18% at 10% 12%, rgba(70,110,40,0.95) 0%, rgba(70,110,40,0) 100%),
      radial-gradient(ellipse 30% 30% at 38% 8%, rgba(240,225,200,0.95) 0%, rgba(240,225,200,0) 100%),
      radial-gradient(ellipse 40% 35% at 22% 45%, rgba(200,40,25,0.95) 0%, rgba(200,40,25,0) 100%),
      radial-gradient(ellipse 30% 40% at 48% 22%, rgba(215,70,40,0.9) 0%, rgba(215,70,40,0) 100%),
      radial-gradient(ellipse 70% 75% at 30% 25%, rgba(210,170,130,0.95) 0%, rgba(150,80,40,0.6) 60%, rgba(30,14,6,0) 100%),
      radial-gradient(ellipse 50% 60% at 85% 15%, rgba(60,34,20,0.9) 0%, rgba(30,14,6,0) 100%);
  }
  .photo--left-pizza {
    left: 0; top: 790px; width: 660px; height: 410px;
    background:
      radial-gradient(ellipse 30% 30% at 30% 45%, rgba(220,120,60,0.95) 0%, rgba(220,120,60,0) 100%),
      radial-gradient(ellipse 20% 20% at 15% 70%, rgba(170,60,35,0.9) 0%, rgba(170,60,35,0) 100%),
      radial-gradient(ellipse 25% 20% at 55% 30%, rgba(120,150,60,0.45) 0%, rgba(120,150,60,0) 100%),
      radial-gradient(ellipse 80% 85% at 35% 50%, rgba(180,85,40,0.95) 0%, rgba(110,50,22,0.8) 55%, rgba(30,14,6,0) 100%);
  }
  .photo--right-pizza {
    left: 580px; top: 620px; width: 268px; height: 430px;
    background:
      radial-gradient(ellipse 35% 20% at 55% 30%, rgba(220,60,40,0.9) 0%, rgba(220,60,40,0) 100%),
      radial-gradient(ellipse 40% 30% at 55% 70%, rgba(240,210,150,0.95) 0%, rgba(240,210,150,0) 100%),
      radial-gradient(ellipse 90% 80% at 70% 50%, rgba(225,175,105,0.95) 0%, rgba(170,100,50,0.7) 55%, rgba(40,18,8,0) 100%);
  }
  .title-band { position: absolute; left: 0; top: 0; width: 848px; height: 560px; }
  .headline {
    position: absolute; left: 0; top: 0; width: 848px; height: 560px;
    font-family: "Alfa Slab One", serif; font-weight: 400;
  }
  .headline svg { width: 848px; height: 560px; display: block; overflow: visible; }
  .headline text {
    fill: var(--title-orange);
    font-size: 118px;
    text-transform: uppercase;
    paint-order: stroke;
    stroke: rgba(40,18,6,0.55);
    stroke-width: 4px;
  }
  .price-tag {
    position: absolute; left: 0; top: 472px; width: 848px;
    text-align: center; line-height: 1;
  }
  .price-tag__inner {
    display: inline-block;
    padding: 6px 30px 12px 22px;
    background: var(--ink);
    border-radius: 34px;
    box-shadow: 0 0 0 4px #2a2a2a;
  }
  .price-tag__dollar {
    font-family: "Kaushan Script", cursive;
    font-size: 100px; color: var(--price-yellow);
  }
  .price-tag__amount {
    font-family: "Fredoka", sans-serif; font-weight: 700;
    font-size: 96px; color: var(--price-yellow);
  }
  .price-tag__item {
    font-family: "Fredoka", sans-serif; font-weight: 700;
    font-size: 96px; color: var(--white);
  }
  .description {
    position: absolute; left: 20px; top: 608px; width: 808px;
    font-family: "Parisienne", cursive;
    font-size: 42px; line-height: 74px;
    color: var(--cream); text-align: center;
    text-shadow: 1px 1px 4px rgba(0,0,0,0.7);
    white-space: nowrap;
  }
  .terms {
    position: absolute; left: 234px; top: 985px;
    font-family: "Archivo Black", sans-serif;
    line-height: 46px;
    white-space: nowrap;
    text-shadow: 3px 3px 0 var(--ink), -3px -3px 0 var(--ink), 3px -3px 0 var(--ink), -3px 3px 0 var(--ink), 0 0 10px var(--ink);
  }
  .terms__service { font-size: 36px; color: var(--white); }
  .terms__size { font-size: 36px; color: var(--price-yellow); }
</style>
</head>
<body>
<main class="poster">
  <div class="photo photo--hero" role="img" aria-label="Close-up photo of a margherita pizza slice with tomato, melted mozzarella and fresh basil"></div>
  <div class="photo photo--left-pizza" role="img" aria-label="Photo of a pizza topped with olives and chopped vegetables"></div>
  <div class="photo photo--right-pizza" role="img" aria-label="Photo of a cheesy pizza with olives and red peppers"></div>

  <svg class="title-band" viewBox="0 0 848 560" aria-hidden="true">
    <path d="M0 330 C 260 260, 540 160, 848 110 L 848 330 C 560 360, 300 420, 0 500 Z" fill="var(--band)" opacity="0.8"/>
    <path d="M0 500 C 300 420, 560 360, 848 330" fill="none" stroke="#6e3616" stroke-width="3" opacity="0.7"/>
  </svg>

  <h1 class="headline">
    <svg viewBox="0 0 848 560" aria-label="Rustico Rush">
      <text x="40" y="395" transform="rotate(-13 40 395)" textLength="785" lengthAdjust="spacing">Rustico</text>
      <text x="385" y="450" transform="rotate(-13 385 450)" textLength="445" lengthAdjust="spacing">Rush</text>
    </svg>
  </h1>

  <div class="price-tag">
    <div class="price-tag__inner"><span class="price-tag__dollar">$</span><span class="price-tag__amount">9</span><span class="price-tag__item">Pizza</span></div>
  </div>

  <p class="description">Crispy and fresh dough topped with mouth watering<br>mozzarella cheese and sprinkled with oregano and<br>finished with fresh basil</p>

  <div class="terms">
    <p class="terms__service">takeaway &amp; eat in only</p>
    <p class="terms__size">Medium Pizza Only (11 inch)</p>
  </div>
</main>
</body>
</html>
```